Book Cover Design - Uncovering Weight Loss Secrets

I need a book cover design for a book called 'Folding The Map'. It is a book that goes through all of the secrets to weight loss, without any crazy shakes or workouts or pills or potions. The book is really focused on helping people understand that Weight loss is simple and has more to do with our mindset as well as the food we were eating. It is about taking personal responsibility not looking for the next fancy revolutionary product that is going to help them magically melt the fat away. The book is pragmatic in nature and breaks down in simple terms how we can lose weight and keep it off for the rest of our lives. It shows the user that it is simple to lose weight, but it takes effort. They should stop looking for a quick fix when it comes to weight loss but instead eat healthy for the rest of their lives.
The book is intended to be hard-hitting no holds barred approach. The book has the same title as my business name. I will attach the current logo that we use in the business. This doesn't need to be on the front of the book maybe at the back down the bottom somewhere.
I am looking to have both an e-book cover and a standard printed book cover.
I don't have any colours in mind, my logo can be adapted to be different colours or just white.
The message that I am wanting people to feel when they see my book, is that all these Weightloss fads are a joke, that I know the secrets that will get them to their weight loss goal even if they fail at everything else before.
On the cover it should say the following.
FOLDING THE MAP
Uncovering the Weight Loss Secrets
The big companies have been trying to keep hidden for years!
COLIN MAYHEW
People who have failed many times trying to lose weight & need help
Weight Loss

```html
<!DOCTYPE html>
<html lang="en">
<head>
<meta charset="utf-8">
<title>Folding The Map — Book Cover</title>
<link href="https://fonts.googleapis.com/css2?family=Anton&family=Bebas+Neue&family=Dancing+Script:wght@700&family=Oswald:wght@500;600&display=swap" rel="stylesheet">
<style>
  :root {
    --page: #ffffff;
    --cover-pink: #f4e4ee;
    --accent-pink: #e8006a;
    --ink: #101a28;
    --text-black: #0a0a0a;
    --white: #ffffff;
    --photo-light: #ead0dc;
    --photo-mid: #c98a80;
    --photo-dark: #2f3a45;
  }
  * { margin: 0; padding: 0; box-sizing: border-box; }
  html, body {
    width: 1200px; height: 1200px;
    overflow: hidden;
    background: var(--page);
  }
  .cover {
    position: absolute;
    left: 257px; top: 42px;
    width: 686px; height: 1117px;
    background: var(--cover-pink);
    overflow: hidden;
  }
  .cover-photo {
    position: absolute;
    left: 0; top: 324px;
    width: 348px; height: 689px;
    background:
      radial-gradient(ellipse 40% 22% at 50% 14%, #d9a993 0%, rgba(217,169,147,0) 100%),
      linear-gradient(180deg, var(--photo-light) 0%, var(--photo-mid) 45%, var(--photo-mid) 65%, var(--photo-dark) 100%);
    border-radius: 60px 60px 0 0;
  }
  .title-main {
    position: absolute;
    left: 0; right: 0; top: 34px;
    text-align: center;
    font-family: "Anton", sans-serif;
    font-size: 196px;
    line-height: 1;
    letter-spacing: 2px;
    color: var(--ink);
  }
  .title-script {
    position: absolute;
    left: 0; right: 0; top: 190px;
    text-align: center;
    font-family: "Dancing Script", cursive;
    font-weight: 700;
    font-size: 168px;
    line-height: 1;
    color: var(--accent-pink);
    transform: rotate(-4deg);
  }
  .badge {
    position: absolute;
    left: 371px; top: 377px;
    width: 238px; height: 238px;
  }
  .badge svg { position: absolute; inset: 0; }
  .badge-text {
    position: absolute; inset: 0;
    display: flex; flex-direction: column; justify-content: center; align-items: center;
    font-family: "Bebas Neue", sans-serif;
    font-size: 50px;
    line-height: 0.96;
    color: var(--white);
    text-align: center;
  }
  .subtitle {
    position: absolute;
    right: 70px; top: 648px;
    text-align: right;
    font-family: "Bebas Neue", sans-serif;
    font-size: 47px;
    line-height: 0.99;
    color: var(--text-black);
  }
  .author-band {
    position: absolute;
    left: 0; bottom: 0;
    width: 686px; height: 104px;
    background: var(--accent-pink);
    display: flex; align-items: center; justify-content: center;
  }
  .author-name {
    font-family: "Oswald", sans-serif;
    font-weight: 600;
    font-size: 50px;
    letter-spacing: 24px;
    margin-right: -24px;
    color: var(--white);
  }
</style>
</head>
<body>
  <main class="cover">
    <div class="cover-photo" role="img" aria-label="Photo of a surprised young woman in a rose tank top holding a bathroom scale"></div>
    <h1 class="title-main">FOLDING</h1>
    <div class="title-script">The Map</div>
    <div class="badge">
      <svg viewBox="0 0 240 240" width="238" height="238" aria-hidden="true">
        <polygon fill="var(--accent-pink)" points="240,120 222,140.3 230.9,166 206.4,177.8 204.8,204.8 177.8,206.4 166,230.9 140.3,222 120,240 99.7,222 74,230.9 62.2,206.4 35.2,204.8 33.6,177.8 9.1,166 18,140.3 0,120 18,99.7 9.1,74 33.6,62.2 35.2,35.2 62.2,33.6 74,9.1 99.7,18 120,0 140.3,18 166,9.1 177.8,33.6 204.8,35.2 206.4,62.2 230.9,74 222,99.7"/>
      </svg>
      <div class="badge-text"><span>WEIGHT</span><span>LOSS</span><span>SECRETS</span></div>
    </div>
    <p class="subtitle">FOR LOSING ALL THE<br>WEIGHT YOU WANT<br>&amp; KEEPING IT OFF<br>FOREVER<br>NO MATTER WHAT<br>YOU HAVE TRIED IN<br>THE PAST</p>
    <footer class="author-band">
      <span class="author-name">COLIN MAYHEW</span>
    </footer>
  </main>
</body>
</html>
```